Home Visiting Physiotherapy Promotion Flyer

DL flyer for a home visiting/mobile physiotherapy business/service..

Needs to be eye catching and leave impression on people's mind
Need to emphasise that we are a Mobile service.
Need to emphasise that all of our appointments are extended visits for 30 minutes rather than the regular 15-20 minutes that other physios offer.

Quality and reliable service,

Services provided:
At Brindle Care Physio we provide comprehensive physiotherapy assessments and treatments for patients requiring a physiotherapist to be seen in the comfort and privacy of their own home.

- Aged care
- Falls prevention
- Help older people stay independent for longer
- Musculoskeletal (sore neck/hip/back/knee/headaches)
- Post admission rehabilitation
- Orthopaedic rehabilitation (knee/shoulder/hip/back/neck/hand/foot)
- Neurological rehabilitation (spinal injuries, Parkinson’s disease, stroke, MS)
- Dry needling

Brindle Care Physio contact details:
Mob: 0491 572 806
Email: clara@brindlecarephysio.com.au

Our Catch phrase is
Brindle Care Physio
“The Home Visiting Specialists”

Our orange colour is 244 119 33 and grey.
Logo attached.

Something similar to this http://www.sketchforum.com/design/4172359 Please note that this flyer (the business whom the flyer was designed for) is very close to where we are located so it needs to be different enough to differentiate them from us.
Updates

Target Market(s)

Anyone that finds it hard to get out of the house to visit a physiotherapist. e.g. the elderly, immobile, mothers who find it hard to leave their house with their baby, anyone who needs a carer/family member/taxi to be transported to a physical practice. The elderly (over 65's), BSR (Bureau of Service Retirees - no charge to client), busy working adults (can come to workplace), busy families, people with disabilities, people that have just had an operation, neurological disorders (eg. Parkinson's, stroke, amputees)

Industry/Entity Type

Business

Font styles to use
Sans Serif

Requirements
Must have
• Extended consultations – 30 min
• Mobile, home visiting service
• Phone Number (both mobile and land line)
• Accept BSR, Enhanced Care Plans and CLQF clients
• GTK Member – Please use the GTK logo as attached
• Our Brindle Care Physio logo – as attached, with slogan “The Home Visiting Specialists”
• 25% discount for your initial consultation if you mention this ad

```html
<!DOCTYPE html>
<html lang="en">
<head>
<meta charset="utf-8">
<title>Brindle Care Physio – DL Flyer</title>
<link rel="stylesheet" href="https://fonts.googleapis.com/css2?family=Catamaran:wght@400;500;600;700;800&display=swap">
<style>
  :root {
    --orange: #f47721;
    --orange-deep: #e0661a;
    --grey: #555759;
    --grey-mid: #6d6f71;
    --grey-light: #9a9c9e;
    --ink: #1d1d1d;
    --paper: #ffffff;
    --stage: #dcdcdc;
    --photo-a: #d9dde2;
    --photo-b: #b9c4cf;
  }
  * { box-sizing: border-box; margin: 0; padding: 0; }
  html, body { width: 1200px; height: 960px; overflow: hidden; }
  body {
    background: var(--stage);
    font-family: "Catamaran", Arial, sans-serif;
    position: relative;
  }
  .flyer {
    position: absolute;
    width: 410px;
    height: 820px;
    background: var(--paper);
    overflow: hidden;
    box-shadow: 0 6px 18px rgba(0,0,0,.25);
  }
  .flyer--front { left: 147px; top: 70px; }
  .flyer--back  { left: 643px; top: 70px; }
  .flyer svg.art { position: absolute; inset: 0; }

  /* FRONT */
  .brand {
    position: absolute; top: 50px; left: 0; width: 100%;
    text-align: center;
    font-size: 36px; font-weight: 500; color: var(--orange);
    letter-spacing: .3px;
  }
  .discount {
    position: absolute; left: 240px; top: 320px;
    width: 146px; height: 146px; border-radius: 50%;
    background: var(--orange);
    border: 3px solid var(--paper);
    box-shadow: 0 0 0 6px var(--grey-mid);
    color: var(--paper); text-align: center;
    display: flex; flex-direction: column; align-items: center; justify-content: center;
  }
  .discount__value { font-size: 50px; font-weight: 800; line-height: .9; }
  .discount__label { font-size: 21px; font-weight: 800; line-height: 1.1; }
  .discount__note { font-size: 12.5px; font-weight: 500; line-height: 1.2; letter-spacing: .3px; }
  .tagline {
    position: absolute; top: 490px; left: 0; width: 100%; text-align: center;
  }
  .tagline__lead { font-size: 34px; font-weight: 800; color: var(--grey); line-height: 1; letter-spacing: .5px; }
  .tagline__main { font-size: 54px; font-weight: 800; color: var(--orange); line-height: 1; margin-top: 4px; letter-spacing: .5px; }
  .tagline__sub { font-size: 26px; font-weight: 500; color: var(--ink); line-height: 1; margin-top: 8px; }
  .extended-band {
    position: absolute; top: 637px; left: 0; width: 100%; height: 95px;
    background: linear-gradient(180deg, #8c8e90 0%, #6c6e70 100%);
    color: var(--paper); text-align: center;
    display: flex; flex-direction: column; justify-content: center;
    font-size: 19px; font-weight: 500; line-height: 1.22; letter-spacing: .4px;
  }
  .call-bar {
    position: absolute; left: 0; top: 760px; width: 100%; height: 61px;
  }
  .call-bar__tab {
    position: absolute; left: 0; top: 0; width: 188px; height: 61px;
    background: var(--orange);
    clip-path: polygon(0 0, 85% 0, 100% 100%, 0 100%);
    color: var(--paper); padding: 8px 0 0 26px; line-height: 1;
  }
  .call-bar__tab .l1 { display: block; font-size: 22px; font-weight: 500; }
  .call-bar__tab .l2 { display: block; font-size: 18px; font-weight: 800; margin-top: 3px; }
  .call-bar__phone {
    position: absolute; left: 190px; top: 12px;
    font-size: 30px; font-weight: 800; color: var(--grey); letter-spacing: .5px;
  }

  /* BACK */
  .section-tab {
    position: absolute; left: 0; top: 226px; width: 136px; height: 32px;
    background: var(--grey-mid); border-radius: 0 16px 16px 0;
    color: var(--paper); font-weight: 800; font-size: 20px;
    padding: 3px 0 0 28px; letter-spacing: .5px;
  }
  .section-title {
    position: absolute; left: 148px; top: 230px;
    color: var(--orange); font-size: 17px; font-weight: 600;
  }
  .intro {
    position: absolute; left: 28px; top: 272px; width: 332px;
    font-size: 13px; line-height: 1.22; color: var(--ink); text-align: justify;
  }
  .services {
    position: absolute; top: 358px; list-style: none;
    font-size: 11.5px; line-height: 1.25; color: var(--grey);
  }
  .services--left { left: 32px; width: 150px; }
  .services--right { left: 202px; width: 170px; }
  .services li { position: relative; padding-left: 20px; margin-bottom: 8px; }
  .services li svg { position: absolute; left: 0; top: 2px; width: 10px; height: 10px; }
  .accepts {
    position: absolute; top: 524px; left: 0; width: 100%; text-align: center;
    font-size: 20px; line-height: 1.22; color: var(--grey); font-weight: 500;
  }
  .contact {
    position: absolute; top: 672px; left: 0; width: 100%; text-align: center; color: var(--ink);
  }
  .contact__title { font-size: 19px; font-weight: 500; line-height: 1.2; letter-spacing: .3px; }
  .contact__icon { display: block; margin: 8px auto 2px; width: 12px; height: 12px; }
  .contact__phone { font-size: 20px; font-weight: 500; letter-spacing: .6px; line-height: 1.1; }
  .contact__email { font-size: 19px; font-weight: 500; line-height: 1.1; }
</style>
</head>
<body>

<!-- FRONT -->
<section class="flyer flyer--front">
  <svg class="art" viewBox="0 0 410 820" width="410" height="820">
    <defs>
      <linearGradient id="frontPhoto" x1="0" y1="0" x2="1" y2="1">
        <stop offset="0" stop-color="#eef0f2"/>
        <stop offset=".5" stop-color="#c9d3dd"/>
        <stop offset="1" stop-color="#e6e7e8"/>
      </linearGradient>
    </defs>
    <rect x="0" y="104" width="410" height="380" fill="url(#frontPhoto)" role="img" aria-label="Photo: physiotherapist in blue scrubs guiding an older man through an arm exercise with a small dumbbell"/>
    <path d="M60,420 C160,462 300,462 410,418 L410,448 C300,488 160,480 60,420 Z" fill="var(--grey-mid)"/>
    <path d="M0,382 C40,470 210,505 410,452 L410,470 C230,520 60,505 0,448 Z" fill="var(--orange)"/>
    <path d="M0,448 C60,505 230,520 410,470 L410,490 L0,490 Z" fill="var(--paper)"/>
  </svg>

  <div class="brand">Brindle Care Physio</div>

  <div class="discount">
    <span class="discount__value">25%</span>
    <span class="discount__label">DISCOUNT</span>
    <span class="discount__note">FOR YOUR INITIAL<br>CONSULTATION</span>
  </div>

  <div class="tagline">
    <div class="tagline__lead">THE HOME VISITING</div>
    <div class="tagline__main">SPECIALISTS</div>
    <div class="tagline__sub">Mobile, home visiting service</div>
  </div>

  <div class="extended-band">
    <span>OUR APPOINTMENTS ARE EXTENDED</span>
    <span>VISITS FOR 30 MINUTES RATHER THAN</span>
    <span>THE REGULAR 15-20 MINUTES</span>
  </div>

  <div class="call-bar">
    <div class="call-bar__tab"><span class="l1">CALL US FOR</span><span class="l2">CONSULTATION</span></div>
    <div class="call-bar__phone">0491 572 806</div>
  </div>
</section>

<!-- BACK -->
<section class="flyer flyer--back">
  <svg class="art" viewBox="0 0 410 820" width="410" height="820">
    <defs>
      <linearGradient id="backPhoto" x1="0" y1="0" x2="1" y2="1">
        <stop offset="0" stop-color="#f1f2f3"/>
        <stop offset=".55" stop-color="#cfd6dc"/>
        <stop offset="1" stop-color="#8fc9d0"/>
      </linearGradient>
    </defs>
    <rect x="0" y="0" width="410" height="196" fill="url(#backPhoto)" role="img" aria-label="Photo: physiotherapist stretching the leg of a man lying on a treatment table"/>
    <rect x="0" y="196" width="410" height="9" fill="var(--orange)"/>
    <rect x="0" y="205" width="410" height="3" fill="var(--grey-light)"/>
    <path d="M0,740 C40,640 220,570 410,655 L410,820 L0,820 Z" fill="var(--orange)"/>
    <path d="M40,702 C120,640 280,612 410,662 L410,820 L40,820 Z" fill="var(--grey-mid)"/>
    <path d="M0,760 C80,682 300,640 410,712 L410,820 L0,820 Z" fill="var(--paper)"/>
  </svg>

  <div class="section-tab">SERVICE</div>
  <div class="section-title">Quality and reliable service</div>

  <p class="intro">At Brindle Care Physio we provide comprehensive physiotherapy assessments and treatments for patients requiring a physiotherapist to be seen in the comfort and privacy of their own home.</p>

  <ul class="services services--left">
    <li><svg viewBox="0 0 10 10"><rect x=".5" y=".5" width="9" height="9" fill="none" stroke="var(--orange)"/><path d="M2.3,5 L4.3,7 L7.8,2.8" fill="none" stroke="var(--orange)" stroke-width="1.3"/></svg>Aged care</li>
    <li><svg viewBox="0 0 10 10"><rect x=".5" y=".5" width="9" height="9" fill="none" stroke="var(--orange)"/><path d="M2.3,5 L4.3,7 L7.8,2.8" fill="none" stroke="var(--orange)" stroke-width="1.3"/></svg>Falls prevention</li>
    <li><svg viewBox="0 0 10 10"><rect x=".5" y=".5" width="9" height="9" fill="none" stroke="var(--orange)"/><path d="M2.3,5 L4.3,7 L7.8,2.8" fill="none" stroke="var(--orange)" stroke-width="1.3"/></svg>Help older people stay independent for longer</li>
    <li><svg viewBox="0 0 10 10"><rect x=".5" y=".5" width="9" height="9" fill="none" stroke="var(--orange)"/><path d="M2.3,5 L4.3,7 L7.8,2.8" fill="none" stroke="var(--orange)" stroke-width="1.3"/></svg>Musculoskeletal (sore neck/hip/back/knee/ headaches)</li>
  </ul>

  <ul class="services services--right">
    <li><svg viewBox="0 0 10 10"><rect x=".5" y=".5" width="9" height="9" fill="none" stroke="var(--orange)"/><path d="M2.3,5 L4.3,7 L7.8,2.8" fill="none" stroke="var(--orange)" stroke-width="1.3"/></svg>Post admission rehabilitation</li>
    <li><svg viewBox="0 0 10 10"><rect x=".5" y=".5" width="9" height="9" fill="none" stroke="var(--orange)"/><path d="M2.3,5 L4.3,7 L7.8,2.8" fill="none" stroke="var(--orange)" stroke-width="1.3"/></svg>Orthopaedic rehabilitation (knee/shoulder/hip/back/ neck/hand/foot)</li>
    <li><svg viewBox="0 0 10 10"><rect x=".5" y=".5" width="9" height="9" fill="none" stroke="var(--orange)"/><path d="M2.3,5 L4.3,7 L7.8,2.8" fill="none" stroke="var(--orange)" stroke-width="1.3"/></svg>Neurological rehabilitation (spinal injuries, Parkinson’s disease, stroke, MS)</li>
    <li><svg viewBox="0 0 10 10"><rect x=".5" y=".5" width="9" height="9" fill="none" stroke="var(--orange)"/><path d="M2.3,5 L4.3,7 L7.8,2.8" fill="none" stroke="var(--orange)" stroke-width="1.3"/></svg>Dry needling</li>
  </ul>

  <p class="accepts">Accept BSR, Enhanced Care Plans<br>and CLQF clients</p>

  <div class="contact">
    <div class="contact__title">BRINDLE CARE PHYSIO<br>CONTACT DETAILS:</div>
    <svg class="contact__icon" viewBox="0 0 12 12" aria-hidden="true"><path d="M1,4 C1,1.5 11,1.5 11,4 L9,5 L8,3.5 L4,3.5 L3,5 Z M2.5,6 L9.5,6 L10.5,11 L1.5,11 Z" fill="var(--orange)"/></svg>
    <div class="contact__phone">0491 572 806</div>
    <svg class="contact__icon" viewBox="0 0 12 12" aria-hidden="true"><rect x="0" y="2" width="12" height="8" fill="var(--orange)"/><path d="M0,2 L6,7 L12,2" fill="none" stroke="var(--paper)" stroke-width="1"/></svg>
    <div class="contact__email">clara@brindlecarephysio.com.au</div>
  </div>
</section>

</body>
</html>
```